Ridge Fern Electical winter special

I need an ad for a print magazine for my electrical contracting business.
It must have my logo and business name as the main back ground with a banner over the top stating 'winter solar special 10% off'
it must have my licence number in the botomm right corner lic.472915K
It must have my name Derek Whitlam ph 0438215976
Also I would like it to say somewher 'Call now for your free solar assessment'
I would like it on a sharp black bagground like my business card attached and flyer attached
This will be a in a landscape design not potrait
Target Market(s)
Print ad and banner advertising
Industry/Entity Type
Solar Energy
Colors
Designer to choose colors to be used in the design.
Requirements
Must have
- my licence number on bottom right corner
- lic.472915K

```html
<!DOCTYPE html>
<html lang="en">
<head>
<meta charset="utf-8">
<title>Ridge Fern Electical – Winter Solar Special</title>
<link rel="stylesheet" href="https://fonts.googleapis.com/css2?family=Bebas+Neue&family=Oswald:wght@500&family=Montserrat:wght@500&family=Open+Sans:wght@400&display=swap">
<style>
  :root {
    --page-bg: #bdbdbd;
    --ink-dark: #2a2a2a;
    --sky-light: #d9d9d9;
    --sky-mid: #8a8a8a;
    --brand-green: #7cc22f;
    --white: #ffffff;
  }
  html, body {
    margin: 0;
    width: 801px;
    height: 1200px;
    overflow: hidden;
    background: radial-gradient(ellipse at 50% 40%, #d6d6d6 0%, var(--page-bg) 70%, #a9a9a9 100%);
  }
  .ad {
    position: absolute;
    left: 25px;
    top: 310px;
    width: 750px;
    height: 580px;
    background: var(--ink-dark);
    overflow: hidden;
    box-shadow: 0 18px 22px -14px rgba(0,0,0,.55);
  }
  .ad__photo {
    position: absolute;
    inset: 0;
    background:
      radial-gradient(ellipse 45% 30% at 15% 72%, rgba(255,255,255,.55), transparent 70%),
      radial-gradient(ellipse 30% 22% at 62% 55%, #4a4a4a, transparent 75%),
      linear-gradient(180deg, var(--ink-dark) 0%, #3a3a3a 35%, var(--sky-mid) 62%, var(--sky-light) 82%, #9c9c9c 100%);
  }
  .offer-frame {
    position: absolute;
    left: 45px;
    top: 38px;
    width: 268px;
    height: 269px;
    border: 1px solid var(--white);
    box-sizing: border-box;
  }
  .offer-title {
    position: absolute;
    left: 60px;
    margin: 0;
    font-family: "Bebas Neue", "Oswald", sans-serif;
    font-weight: 400;
    color: var(--white);
    line-height: 1;
    white-space: nowrap;
  }
  .offer-title--winter { top: 48px; font-size: 94px; letter-spacing: 1px; }
  .offer-title--solar { top: 130px; font-size: 47px; }
  .offer-title--discount { top: 180px; font-size: 92px; color: var(--brand-green); }
  .offer-banner {
    position: absolute;
    left: 24px;
    top: 269px;
    width: 308px;
    height: 23px;
    background: var(--brand-green);
    font-family: "Open Sans", sans-serif;
    font-size: 12.5px;
    color: var(--white);
    line-height: 23px;
    text-align: center;
    white-space: nowrap;
  }
  .brand {
    position: absolute;
    left: 455px;
    top: 40px;
    width: 270px;
    text-align: center;
    color: var(--brand-green);
    font-family: "Montserrat", sans-serif;
    font-weight: 500;
  }
  .brand__dot {
    width: 64px;
    height: 64px;
    margin: 0 auto 14px;
    border-radius: 50%;
    background: var(--brand-green);
  }
  .brand__name {
    font-size: 32px;
    line-height: 1;
    letter-spacing: 1px;
  }
  .brand__sub {
    margin-top: 4px;
    font-size: 14px;
    letter-spacing: 7px;
  }
  .contact-bar {
    position: absolute;
    left: 0;
    bottom: 0;
    width: 750px;
    height: 60px;
  }
  .contact-text {
    position: absolute;
    left: 22px;
    bottom: 18px;
    font-family: "Oswald", sans-serif;
    font-weight: 500;
    font-size: 22px;
    color: var(--white);
    display: flex;
    align-items: center;
    gap: 10px;
    white-space: nowrap;
  }
  .contact-text__divider { width: 1px; height: 24px; background: var(--white); }
  .licence {
    position: absolute;
    right: 38px;
    bottom: 4px;
    font-family: "Open Sans", sans-serif;
    font-size: 15px;
    color: var(--white);
  }
</style>
</head>
<body>
  <section class="ad">
    <div class="ad__photo" role="img" aria-label="Black and white photo of a large solar panel array on a stand in a grassy field under a cloudy sky"></div>

    <div class="offer-frame"></div>
    <h1 class="offer-title offer-title--winter">WINTER</h1>
    <p class="offer-title offer-title--solar">SOLAR SPECIAL</p>
    <p class="offer-title offer-title--discount">10% OFF</p>
    <div class="offer-banner">CALL NOW FOR YOUR FREE SOLAR ASSESSMENT</div>

    <div class="brand">
      <div class="brand__dot"></div>
      <div class="brand__name">RIDGE FERN</div>
      <div class="brand__sub">ELECTICAL</div>
    </div>

    <svg class="contact-bar" viewBox="0 0 750 60" aria-hidden="true">
      <polygon points="0,0 365,0 385,32 750,32 750,60 0,60" fill="var(--brand-green)"/>
    </svg>
    <div class="contact-text">
      <span>DEREK WHITLAM</span>
      <span class="contact-text__divider"></span>
      <svg width="14" height="22" viewBox="0 0 14 22" aria-hidden="true">
        <rect x="1" y="1" width="12" height="20" rx="2" fill="none" stroke="#fff" stroke-width="1.6"/>
        <line x1="5" y1="18" x2="9" y2="18" stroke="#fff" stroke-width="1.4"/>
      </svg>
      <span>0438215976</span>
    </div>
    <div class="licence">lic.472915K</div>
  </section>
</body>
</html>
```